Torvane, Inc Business Cards 14

We are an environmental services firm looking for a sharp, eye catching business card design that ties our logo in with our website www.torvane-inc.example. Here are items that MUST be included in the design:
website: www.torvane-inc.example
Employee Name & Title: Please use Brian Marlow, MS Senior Risk Assessor/Marketing as your template
Phone # 555-214-3067 (extensions will need to be added per employee)
Fax # 555-214-3079
email address (will need to be changed with each employees) bmarlow@torvane-inc.example
Address: Quillmere Business Park, 64 Quillmere Street, Suite 2, Dunmore Falls, MA 01920
Consultants, Engineers, Contractors
Servicing all of New England
Solutions Since 1985
ZNU Certified
PDR Contractor
Environmental Consulting, Engineering, Contracting, Compliance and Risk Management
Our logo, FOBLI logo, TQC logo, and PDR logo must appear on the card
We are looking for a card that will really POP.
Updates
Good Morning Designers,
Reason: I have not received a design that combines both the website and logo colors in the exact way that I want.
Target Market(s)
Our primary markets are: banks, law firms, municipalities, federal government, and petroleum companies.
Industry/Entity Type
Business
Requirements
Must have
- Here are items that MUST be included in the design:
website: www.torvane-inc.example
Fax # 555-214-3079
Solutions Since 1985
ZNU Certified
PDR Contractor

```html
<!DOCTYPE html>
<html lang="en">
<head>
<meta charset="utf-8">
<title>Torvane, Inc – Business Card</title>
<link rel="stylesheet" href="https://fonts.googleapis.com/css2?family=Open+Sans:wght@400;700&family=Fira+Sans+Condensed:wght@400;500&display=swap">
<style>
  :root {
    --paper: #ffffff;
    --white: #ffffff;
    --teal: #0f97a8;
    --rust: #8e3b1c;
    --badge-blue: #1d5d8a;
  }
  * { box-sizing: border-box; margin: 0; padding: 0; }
  html, body {
    width: 1200px; height: 1000px; overflow: hidden;
    background: var(--paper);
  }
  .card {
    position: absolute; top: 115px; width: 419px; height: 756px; overflow: hidden;
    color: var(--white);
  }
  .card-front { left: 82px; font-family: "Open Sans", Arial, sans-serif; }
  .card-back { left: 705px; font-family: "Fira Sans Condensed", "Arial Narrow", sans-serif; }
  .card-bg { position: absolute; inset: 0; }

  /* front */
  .website { position: absolute; top: 24px; right: 24px; font-weight: 700; font-size: 22px; white-space: nowrap; }
  .employee-name { position: absolute; top: 214px; left: 27px; font-weight: 700; font-size: 31px; }
  .employee-title { position: absolute; top: 257px; left: 27px; font-size: 18px; }
  .contact, .address {
    position: absolute; left: 60px; font-size: 18px; line-height: 28.5px; white-space: nowrap;
  }
  .contact { top: 388px; }
  .address { top: 499px; }
  .brand-name {
    position: absolute; font-weight: 700; color: var(--teal); white-space: nowrap;
  }
  .card-front .brand-name { top: 612px; right: 28px; font-size: 42px; }
  .tagline {
    position: absolute; bottom: 16px; left: 0; right: 0; text-align: center;
    font-weight: 700; font-size: 17px; letter-spacing: 1.6px;
  }

  /* back */
  .card-back .brand-name { top: 28px; left: 32px; font-size: 54px; font-weight: 500; }
  .services { position: absolute; top: 354px; left: 110px; list-style: none; font-size: 24.5px; line-height: 32.7px; }
  .services li { position: relative; }
  .services li::before {
    content: ""; position: absolute; left: -25px; top: 13px; width: 9px; height: 9px;
    border-radius: 50%; background: var(--white);
  }
  .badge { position: absolute; }
  .badge-rating { left: 22px; top: 518px; width: 51px; height: 90px; background: var(--badge-blue); border: 2px solid var(--white); border-radius: 4px; }
  .badge-contract { left: 103px; top: 563px; width: 167px; height: 47px; background: var(--white); border-left: 42px solid var(--badge-blue); }
  .badge-certified { left: 284px; top: 561px; width: 116px; height: 50px; background: var(--white); border: 2px solid var(--teal); border-radius: 6px; }
  .rust-band { position: absolute; left: 0; top: 640px; width: 419px; height: 22px; background: var(--rust); }
  .footer-lines { position: absolute; top: 674px; left: 0; right: 0; text-align: center; font-size: 23px; line-height: 32px; }
</style>
</head>
<body>

<section class="card card-front">
  <svg class="card-bg" width="419" height="756" role="img" aria-label="Close-up photograph of a green blade of grass with water droplets on a blurred green background">
    <defs>
      <linearGradient id="frontPhoto" x1="0" y1="0" x2="0.3" y2="1">
        <stop offset="0" stop-color="#2f7d16"/>
        <stop offset="0.15" stop-color="#8fd047"/>
        <stop offset="0.45" stop-color="#6cc237"/>
        <stop offset="0.62" stop-color="#2f8a1c"/>
        <stop offset="0.8" stop-color="#55b32a"/>
        <stop offset="1" stop-color="#0f3f0a"/>
      </linearGradient>
      <radialGradient id="frontGlow" cx="0.95" cy="0.02" r="0.35">
        <stop offset="0" stop-color="#d8f79a" stop-opacity="0.9"/>
        <stop offset="1" stop-color="#d8f79a" stop-opacity="0"/>
      </radialGradient>
    </defs>
    <rect width="419" height="756" fill="url(#frontPhoto)"/>
    <rect width="419" height="756" fill="url(#frontGlow)"/>
  </svg>

  <div class="website">www.torvane-inc.example</div>
  <h1 class="employee-name">Brian Marlow</h1>
  <p class="employee-title">MS Senior Risk Assessor/Marketing</p>

  <p class="contact">
    Phone # 555-214-3067<br>
    Fax # 555-214-3079<br>
    Email: bmarlow@torvane-inc.example
  </p>
  <p class="address">
    Quillmere Business Park,<br>
    64 Quillmere Street, Suite 2,<br>
    Dunmore Falls, MA 01920
  </p>

  <div class="brand-name">Torvane, Inc</div>
  <p class="tagline">Consultants, Engineers, Contractors</p>
</section>

<section class="card card-back">
  <svg class="card-bg" width="419" height="756">
    <defs>
      <linearGradient id="backBase" x1="0" y1="0" x2="0" y2="1">
        <stop offset="0" stop-color="#566b20"/>
        <stop offset="1" stop-color="#4a6a28"/>
      </linearGradient>
      <linearGradient id="backPhoto" x1="0" y1="0" x2="1" y2="1">
        <stop offset="0" stop-color="#7f9a3a"/>
        <stop offset="0.5" stop-color="#8fb24a"/>
        <stop offset="1" stop-color="#5d7a22"/>
      </linearGradient>
    </defs>
    <rect width="419" height="756" fill="url(#backBase)"/>
    <path role="img" aria-label="Close-up photograph of a green leaf covered in water droplets"
          d="M0 0 H419 V335 C330 295 220 270 120 275 C70 278 30 282 0 290 Z" fill="url(#backPhoto)"/>
  </svg>

  <div class="brand-name">Torvane, Inc</div>

  <ul class="services">
    <li>Environmental Consulting</li>
    <li>Engineering</li>
    <li>Contracting</li>
    <li>Compliance</li>
    <li>Risk Management</li>
  </ul>

  <div class="badge badge-rating" role="img" aria-label="Accreditation badge"></div>
  <div class="badge badge-contract" role="img" aria-label="Contract holder badge"></div>
  <div class="badge badge-certified" role="img" aria-label="Certification badge"></div>

  <div class="rust-band"></div>

  <p class="footer-lines">Servicing all of New England<br>Solutions Since 1985</p>
</section>

</body>
</html>
```